Modern luxury trendy cosmetics label

Looking for a cosmetics packaging label design. We are looking for a professionel, modern and luxury look like Lorena Vasquel, Meadowkin Apothecary, Marigold Tessin, Gavin Albert Pruke, Zuna, Orvik + Dalle, Velumi, Sleepy Walrus, the plainfold, lumiere de sable.Name of product: Nordic Tulip Mask - Needle-Free Contour Ritual Ingredients that have scientific proof of anti aging: Cherry blossom extact, collegen, hyaluronic acid, coconut oil. Color of product itself: Pastel pink. Smell: Cherry blossom. Colors of label: simple and black and white or some subtle colors.

Target Market(s)

Women, luxury market, modern women, young and old women

Industry/Entity Type

Cosmetics

Font styles to use
Sans Serif

Colors

Designer to choose colors to be used in the design.

Requirements
Must have
• A modern look, professional, cosmetics, beauty, professional market, original

```html
<!DOCTYPE html>
<html lang="en">
<head>
<meta charset="utf-8">
<title>Olvara — Nordic Tulip Mask</title>
<link href="https://fonts.googleapis.com/css2?family=Tenor+Sans&display=swap" rel="stylesheet">
<style>
  :root {
    --pack-pink: #f4dfe0;
    --label-white: #ffffff;
    --ink: #111111;
  }
  * { margin: 0; padding: 0; box-sizing: border-box; }
  html, body {
    width: 1002px;
    height: 1200px;
    overflow: hidden;
    background: var(--pack-pink);
  }
  .package {
    position: relative;
    width: 1002px;
    height: 1200px;
    background: var(--pack-pink);
    font-family: "Tenor Sans", sans-serif;
    color: var(--ink);
  }
  .label {
    position: absolute;
    left: 131px;
    top: 192px;
    width: 749px;
    height: 835px;
    background: var(--label-white);
    border: 7px solid var(--ink);
  }
  .label > * {
    position: absolute;
    left: 0;
    right: 0;
    text-align: center;
    white-space: nowrap;
  }
  .brand-name {
    top: 52px;
    font-size: 62px;
    line-height: 1;
    letter-spacing: 0.01em;
  }
  .product-name {
    top: 190px;
    font-size: 96px;
    line-height: 121px;
    font-weight: 400;
    text-transform: uppercase;
  }
  .product-name span {
    display: block;
    letter-spacing: 0.42em;
    padding-left: 0.42em;
  }
  .tagline {
    top: 598px;
    font-size: 26px;
    letter-spacing: 0.2em;
    padding-left: 0.2em;
    text-transform: uppercase;
  }
  .ingredients {
    top: 700px;
    font-size: 15px;
    line-height: 29px;
    letter-spacing: 0.16em;
    padding-left: 0.16em;
    text-transform: uppercase;
  }
</style>
</head>
<body>
  <main class="package">
    <section class="label">
      <p class="brand-name">olvara</p>
      <h1 class="product-name">
        <span>Nordic</span>
        <span>Tulip</span>
        <span>Mask</span>
      </h1>
      <p class="tagline">Needle-Free Contour Ritual</p>
      <p class="ingredients">Made with anti-aging ingredients: cherry blossom<br>extact, collegen, hyaluronic acid, coconut oil</p>
    </section>
  </main>
</body>
</html>
```